Land Buying Company Needs Letterhead for Direct Mail Marketing to Land Owners

We are looking for a professional letterhead that we will be including in our direct mail marketing. We will be sending this to land owners who may be interested in selling or purchasing land.

The letterhead needs to be editable. Headers and footers would look nice, but we are open. We would want it to include our address, website, phone, and email info. For right now the address to use for design purposes would the following:

Address: 415 Bramwell Avenue #600
Dallas, TX 75219
Website - www.quillridgeacres.example
Email - info@quillridgeacres.example
Phone - 866-402-ACRE

I have attached our logo zip file that we just had done on Pixel Guild. Let me know what questions you have, and thank you.

```html
<!DOCTYPE html>
<html lang="en">
<head>
<meta charset="utf-8">
<title>Quillridge Acres Letterhead</title>
<link rel="stylesheet" href="https://fonts.googleapis.com/css2?family=Montserrat:wght@400;500;600&family=Roboto:wght@400&display=swap">
<style>
  :root {
    --leaf: #8dc63f;
    --forest: #3b5323;
    --ink: #333333;
    --muted: #8a8a8a;
    --paper: #ffffff;
    --backdrop: #d9d9d9;
  }
  * { box-sizing: border-box; margin: 0; padding: 0; }
  html, body { width: 1200px; height: 1200px; overflow: hidden; }
  body { background: var(--backdrop); position: relative; font-family: "Montserrat", sans-serif; }

  .letterhead {
    position: absolute; left: 204px; top: 40px;
    width: 792px; height: 1120px;
    background: var(--paper);
    box-shadow: 0 2px 10px rgba(0,0,0,0.18);
    overflow: hidden;
  }

  .brand {
    position: absolute; left: 266px; top: 46px;
    display: flex; align-items: center; gap: 12px;
  }
  .brand-dot { width: 30px; height: 30px; border-radius: 50%; background: var(--forest); }
  .brand-name {
    font-family: "Montserrat", sans-serif; font-weight: 600;
    font-size: 24px; letter-spacing: 1px; color: var(--leaf);
    white-space: nowrap;
  }

  .recipient { position: absolute; left: 81px; top: 258px; }
  .recipient-label { font-size: 14px; letter-spacing: 2px; color: var(--ink); }
  .recipient-name { margin-top: 8px; font-size: 13px; color: var(--leaf); }
  .recipient-address { margin-top: 6px; font-size: 10.5px; line-height: 17.5px; color: var(--muted); }

  .letter-date { position: absolute; right: 80px; top: 262px; font-size: 10.5px; color: #555; }

  .letter-body {
    position: absolute; left: 81px; top: 402px; width: 631px;
    font-size: 10.6px; line-height: 14px; color: var(--muted);
    text-align: justify;
  }
  .letter-body p + p { margin-top: 14px; }

  .signature { position: absolute; left: 81px; top: 791px; width: 135px; height: 28px;
    background: linear-gradient(90deg, #e6e6e6, #f2f2f2); border-radius: 2px; }
  .signer { position: absolute; left: 79px; top: 834px; }
  .signer-name { font-size: 12.5px; color: var(--ink); letter-spacing: 0.3px; }
  .signer-title { margin-top: 3px; font-size: 9.5px; color: var(--muted); }

  .footer-contact { position: absolute; left: 40px; top: 1040px; font-family: "Roboto", sans-serif; color: var(--forest); }
  .footer-address { font-size: 13px; }
  .footer-links { margin-top: 12px; display: flex; align-items: center; font-size: 13px; }
  .footer-links .item { display: flex; align-items: center; gap: 7px; margin-right: 12px; }
  .footer-links svg { width: 11px; height: 11px; fill: var(--leaf); }

  .footer-band { position: absolute; left: 0; top: 1080px; width: 792px; height: 40px; }
</style>
</head>
<body>
  <main class="letterhead">
    <header class="brand">
      <span class="brand-dot"></span>
      <span class="brand-name">QUILLRIDGE ACRES</span>
    </header>

    <section class="recipient">
      <div class="recipient-label">TO</div>
      <div class="recipient-name">Daniel Okafor</div>
      <div class="recipient-address">
        Human Resources<br>
        Northwind Labs Inc.<br>
        2207-B Linden Park, Harlow<br>
        H41 USA
      </div>
    </section>

    <div class="letter-date">Friday, 01/01/2018</div>

    <article class="letter-body">
      <p>Lorem ipsum dolor sit amet, consectetuer adipiscing elit, sed diam nonmmy nibh euismod tincidunt ut laoreet dolore magna aliquam erat volutpat. Ut wisi enim ad minim veniam, quis nostrud exerci tationmcorper suscipit lobortis nisl ut aliquip ex ea commodo consequat. Duis autem vel eum iriure dolor in hendrerit in vulputate velit esse molestie consequat, vel illum dolore eu feugiat nulla facilisis at vero eros et accumsan et iusto odio dignissim qui blandit praesent luptatum zzril delenit augue duis dolore te feugait nulla facilisi.</p>
      <p>Nam liber tempor cum soluta nobis eleifend option congue nihil imprdiet doming id quod mazim placerat facer possim assum. Typi non habent claritatem insitam;</p>
      <p>Est usus legentis in iis qui facit eorum claritatem.</p>
      <p>Investigationes demonstraverunt lectores legere me lius quod ii legunt saepius. Claritas est etiam processus dynamicus, qui sequitur mutationem consuetudium lectorum. Mirum est notare quam littera gothica, quam nunc putamus parum claram, anteposuerit litterarum formas humanitatis per seacula quarta decima et quinta decima. Eodem modo typi, qui nunc nobis videntur parum clari, fiant sollemnes in futurum.</p>
      <p>consectetuer adipiscing elit, sed diam nonummy nibh euismod tincidunt ut laoreet dolore magna aliquam erat volutpat. Ut wisi enim ad minim veniam, quis nostrud exerci tation ullamcorper suscipit lobortis nisl ut aliquip ex ea commodo consequat. Duis autem vel eum iriure dolor in hendrerit in vulputate velit esse molestie consequat, vel illum dolore eu feugiat nulla facilisis at vero eros et accumsan et iusto odio dignissim qui blandit praesent luptatum zzril delenit augue duis dolore te feugait nulla facilisi.</p>
      <p>Nam liber tempor cum soluta nobis eleifend option congue nihil imperdiet .</p>
    </article>

    <div class="signature" role="img" aria-label="Handwritten signature of Evan Marlowe"></div>
    <div class="signer">
      <div class="signer-name">Evan Marlowe</div>
      <div class="signer-title">Managing Director</div>
    </div>

    <footer class="footer-contact">
      <div class="footer-address">415 Bramwell Avenue #600, Dallas, TX 75219</div>
      <div class="footer-links">
        <span class="item">
          <svg viewBox="0 0 24 24" aria-hidden="true"><path d="M6.6 10.8a15.1 15.1 0 0 0 6.6 6.6l2.2-2.2c.3-.3.7-.4 1-.2 1.1.4 2.3.6 3.6.6.6 0 1 .4 1 1V20c0 .6-.4 1-1 1A17 17 0 0 1 3 4c0-.6.4-1 1-1h3.5c.6 0 1 .4 1 1 0 1.3.2 2.5.6 3.6.1.3 0 .7-.2 1z"/></svg>
          866-402-ACRE
        </span>
        <span class="item">
          <svg viewBox="0 0 24 24" aria-hidden="true"><path d="M2 5h20v14H2z M2 5l10 8 10-8" /></svg>
          info@quillridgeacres.example
        </span>
        <span class="item">
          <svg viewBox="0 0 24 24" aria-hidden="true"><circle cx="12" cy="12" r="10"/></svg>
          www.quillridgeacres.example
        </span>
      </div>
    </footer>

    <svg class="footer-band" viewBox="0 0 792 40" preserveAspectRatio="none" aria-hidden="true">
      <path d="M0 14 H628 Q636 14 641 10 L635 19 H0 Z" fill="var(--forest)"/>
      <path d="M0 28 H632 Q645 28 655 17 Q665 5 685 5 H792 V40 H0 Z" fill="var(--leaf)"/>
    </svg>
  </main>
</body>
</html>
```